Women's Online Clothing Boutique Needs Business Cards

I already have a logo that I would like to use. Some of the things that interest me is black business cards, foil embossed logo, glossy embossed logo, leopard print, no yellow font, rounded edges. I even like just a large logo on the front side with all of my information on the back side.

Contact Information for Business Card

https://silverheron.shopvenlo.com/
https://www.pagelink.net/thesilverheronboutique/
https://www.picfeed.net/thesilverheronboutique/
silverheronboutique@mailora.net

Requirements
Must have
• My Logo
Nice to have
• Leopard Print
Should not have
• No Yellow Font

```html
<!DOCTYPE html>
<html lang="en">
<head>
<meta charset="utf-8">
<title>The Silver Heron Boutique – Business Card</title>
<link rel="stylesheet" href="https://fonts.googleapis.com/css2?family=Ubuntu:wght@500&display=swap">
<style>
  :root {
    --page: #ffffff;
    --navy: #1c2233;
    --navy-deep: #121726;
    --dot-gold: #8a6a2e;
    --copper: #d99a63;
    --copper-light: #eab27d;
    --copper-dark: #c0844f;
    --ink: #1b2130;
  }
  * { margin: 0; padding: 0; box-sizing: border-box; }
  html, body {
    width: 1200px;
    height: 798px;
    overflow: hidden;
    background: var(--page);
  }
  .canvas {
    position: relative;
    width: 1200px;
    height: 798px;
    display: flex;
    align-items: center;
    justify-content: center;
    gap: 40px;
  }
  .card {
    position: relative;
    width: 525px;
    height: 300px;
    border-radius: 10px;
    overflow: hidden;
    box-shadow: 0 6px 18px rgba(0, 0, 0, 0.18);
  }

  /* Back side: contact details */
  .card-back {
    background: linear-gradient(135deg, var(--copper-light), var(--copper) 45%, var(--copper-dark));
  }
  .pattern-band {
    position: absolute;
    left: 0;
    top: 0;
    width: 68px;
    height: 100%;
    background: radial-gradient(circle at 50% 40%, var(--navy), var(--navy-deep));
  }
  .contact-list {
    position: absolute;
    left: 96px;
    bottom: 40px;
    list-style: none;
    font-family: "Ubuntu", sans-serif;
    font-weight: 500;
    font-size: 12.5px;
    letter-spacing: 0.09em;
    color: var(--ink);
  }
  .contact-list li {
    display: flex;
    align-items: center;
    gap: 10px;
    line-height: 22px;
  }
  .contact-marker {
    width: 12px;
    height: 12px;
    border-radius: 50%;
    background: var(--ink);
    flex: none;
  }

  /* Front side: name */
  .card-front {
    background: radial-gradient(circle at 50% 50%, var(--navy) 0%, var(--navy-deep) 100%);
  }
  .dot-field {
    position: absolute;
    inset: 0;
    background: radial-gradient(ellipse at 40% 30%, rgba(138, 106, 46, 0.35), rgba(18, 23, 38, 0) 70%);
  }
  .brand-name {
    position: absolute;
    inset: 0;
    display: flex;
    flex-direction: column;
    align-items: center;
    justify-content: center;
    font-family: "Ubuntu", sans-serif;
    font-weight: 500;
    color: var(--copper);
    text-align: center;
  }
  .brand-name .name {
    font-size: 40px;
    letter-spacing: 0.02em;
    line-height: 1.1;
  }
  .brand-rule {
    width: 380px;
    height: 1px;
    background: var(--copper);
    margin-top: 14px;
  }
</style>
</head>
<body>
  <main class="canvas">
    <section class="card card-back" aria-label="Business card back">
      <div class="pattern-band" role="img" aria-label="Navy band with scattered gold dot pattern"></div>
      <ul class="contact-list">
        <li><span class="contact-marker"></span>https://silverheron.shopvenlo.com/</li>
        <li><span class="contact-marker"></span>https://www.pagelink.net/thesilverheronboutique/</li>
        <li><span class="contact-marker"></span>https://www.picfeed.net/thesilverheronboutique/</li>
        <li><span class="contact-marker"></span>silverheronboutique@mailora.net</li>
      </ul>
    </section>

    <section class="card card-front" aria-label="Business card front">
      <div class="dot-field" role="img" aria-label="Navy background with gold and amber dot pattern"></div>
      <div class="brand-name">
        <span class="name">The Silver Heron Boutique</span>
        <span class="brand-rule"></span>
      </div>
    </section>
  </main>
</body>
</html>
```